Web Design Project

We need a website for a new public relations firm offering PR, advertising, media buying, design and social media. Target clients are professional service firms such as lawyers or CPAs. Looks should be clean and look expensive.

Target Market(s)

Professional service firms. Think business to business companies like consultancy firms.

Industry/Entity Type

Professional Service

Colors

Designer to choose colors to be used in the design.

Requirements
Must have
• Site pages for the purpose of design will include Home, Services, Experience, Bios and Contact Us

```html
<!DOCTYPE html>
<html lang="en">
<head>
<meta charset="utf-8">
<title>Halvern — Marketing · PR · Advertising</title>
<link href="https://fonts.googleapis.com/css2?family=Open+Sans:wght@400;600;700&display=swap" rel="stylesheet">
<style>
:root{
  --blue:#0a7acb;
  --blue-dark:#0867ad;
  --ink:#222;
  --grey:#666;
  --grey-light:#8a8a8a;
  --muted:#9a9a9a;
  --card:#f7f7f7;
  --card-edge:#e3e3e3;
  --band-top:#4a5668;
  --band-bottom:#1f2733;
  --nav:#111;
  --footer:#050505;
  --icon:#8e8e8e;
}
*{margin:0;padding:0;box-sizing:border-box}
html,body{width:1140px;height:1200px;overflow:hidden;background:#fff}
body{position:relative;font-family:"Open Sans",Arial,sans-serif;color:var(--grey)}
.top-rule{position:absolute;left:0;top:0;width:1140px;height:2px;background:var(--blue)}

/* header */
.brand{position:absolute;left:163px;top:18px;width:180px}
.brand-name{font-size:37px;font-weight:400;color:#7d7d7d;letter-spacing:1px;line-height:1}
.brand-tag{margin-top:12px;font-size:9px;color:var(--ink);letter-spacing:.6px;padding-left:18px}
.call{position:absolute;left:669px;top:27px;font-size:16px;color:var(--ink)}
.call a{color:var(--blue);text-decoration:none}
.social{position:absolute;top:25px;left:894px;display:flex;gap:5px}
.social span{width:24px;height:24px;border-radius:50%}
.social .s1{background:#3b5a9a}.social .s2{background:#2aa4dc}.social .s3{background:#c8302a}

.nav{position:absolute;top:75px;left:0;height:33px}
.nav a{position:absolute;top:0;height:33px;line-height:34px;text-align:center;font-size:12.5px;color:#fff;text-decoration:none;background:linear-gradient(#2b2b2b,var(--nav));border-radius:3px 3px 0 0}
.nav a.active{background:var(--blue)}

/* hero */
.band{position:absolute;left:0;top:108px;width:1140px;height:358px;background:linear-gradient(90deg,var(--band-bottom),var(--band-top) 50%,var(--band-bottom))}
.hero{position:absolute;left:164px;top:139px;width:814px;height:380px;background:linear-gradient(180deg,#d9dde2 0%,#b7b2a6 45%,#5b6272 80%,#3d4352 100%);box-shadow:0 12px 18px rgba(0,0,0,.18)}
.hero-title{position:absolute;left:90px;top:146px;width:210px;text-align:center;font-size:34px;font-weight:700;line-height:47px;color:#fff;text-shadow:0 1px 3px rgba(0,0,0,.35)}
.dots{position:absolute;top:536px;left:543px;display:flex;gap:7px}
.dots span{width:10px;height:10px;border-radius:50%;background:#111}
.dots span.on{background:var(--blue)}

/* services */
.card{position:absolute;top:574px;width:188px;height:229px;background:var(--card);border:1px solid #eee;border-bottom:3px solid var(--card-edge);text-align:center}
.card svg{position:absolute;left:50%;top:14px;transform:translateX(-50%)}
.card h3{position:absolute;top:80px;width:100%;font-size:18px;font-weight:400;color:#444}
.card p{position:absolute;top:113px;left:10px;right:10px;font-size:10.6px;line-height:18px;color:var(--grey-light)}
.btn{position:absolute;left:51px;top:180px;width:85px;height:27px;line-height:27px;border-radius:14px;background:var(--blue);color:#fff;font-size:12px;text-decoration:none}

/* welcome */
.video{position:absolute;left:164px;top:846px;width:248px;height:211px;background:radial-gradient(circle at 50% 45%,#5a5a5a,#262626 70%)}
.play{position:absolute;left:102px;top:83px}
.welcome{position:absolute;left:431px;top:840px;width:265px}
.welcome h2{font-size:18px;font-weight:400;color:#555;margin-left:1px}
.welcome h4{margin-top:10px;font-size:15.5px;font-weight:400;color:var(--blue);line-height:24px}
.welcome p{margin-top:10px;font-size:10.6px;line-height:18.7px;color:var(--muted);text-align:justify;padding-left:2px}

.news{position:absolute;left:724px;top:840px;width:251px}
.news h2{font-size:18px;font-weight:400;color:#555;padding-bottom:8px;border-bottom:1px solid #e6e6e6}
.item{position:absolute;left:0;width:251px;height:75px}
.date{position:absolute;left:0;top:0;width:36px;height:75px;background:#f2f2f2;text-align:center}
.date b{display:block;height:37px;line-height:37px;background:#9a9a9a;color:#fff;font-weight:400;font-size:15px}
.date span{display:block;line-height:37px;font-size:10.5px;color:#555}
.item h5{position:absolute;left:50px;top:-2px;font-size:14px;font-weight:400;color:#888;white-space:nowrap}
.item p{position:absolute;left:50px;top:22px;width:201px;font-size:10.3px;line-height:18px;color:var(--muted);text-align:justify}

/* footer */
.footer{position:absolute;left:0;top:1099px;width:1140px;height:101px;background:var(--footer)}
.copy{position:absolute;left:163px;top:23px;font-size:11.5px;color:#9a9a9a}
.flinks{position:absolute;left:164px;top:57px;font-size:11px;color:#9a9a9a}
.flinks a{color:#9a9a9a;text-decoration:none}
.flinks i{font-style:normal;margin:0 7px}
.fsocial{position:absolute;left:894px;top:46px;display:flex;gap:22px}
.fsocial span{width:10px;height:10px;border-radius:50%;background:#3a3a3a}
</style>
</head>
<body>
<div class="top-rule"></div>

<header>
  <div class="brand">
    <div class="brand-name">HALVERN</div>
    <div class="brand-tag">Marketing • PR • Advertising</div>
  </div>
  <div class="call">Call Us : <a href="#">+1 800 555 0142</a></div>
  <div class="social" aria-label="Social links"><span class="s1"></span><span class="s2"></span><span class="s3"></span></div>
  <nav class="nav">
    <a class="active" href="#" style="left:397px;width:78px">Home</a>
    <a href="#" style="left:487px;width:141px">SERVICES</a>
    <a href="#" style="left:640px;width:120px">EXPERIENCE</a>
    <a href="#" style="left:771px;width:86px">BIOS</a>
    <a href="#" style="left:868px;width:109px">CONTACT US</a>
  </nav>
</header>

<div class="band"></div>
<section class="hero" role="img" aria-label="Photo of five smiling business professionals in suits standing in a bright office">
  <div class="hero-title">PUBLIC RELATIONS</div>
</section>
<div class="dots"><span class="on"></span><span></span><span></span><span></span></div>

<section class="services">
  <div class="card" style="left:164px">
    <svg width="44" height="56" viewBox="0 0 44 56" fill="var(--icon)"><circle cx="10" cy="6" r="5"/><circle cx="34" cy="6" r="5"/><path d="M3 14h14l5 12 5-12h14v42h-6V30l-9 14h-8l-9-14v26H3z"/></svg>
    <h3>Public Relations</h3>
    <p>Lorem ipsum dolor sit amet, consectetur adipiscing elit, sed do eiusmod tempor incididunt</p>
    <a class="btn" href="#">Read More</a>
  </div>
  <div class="card" style="left:373px">
    <svg width="56" height="58" viewBox="0 0 56 58" fill="var(--icon)"><path d="M2 22h12v20H2z"/><path d="M16 22l34-20v54L16 42z"/><path d="M8 44h8l2 14h-8z"/></svg>
    <h3>Advertising</h3>
    <p>Lorem ipsum dolor sit amet, consectetur adipiscing elit, sed do eiusmod tempor incididunt</p>
    <a class="btn" href="#">Read More</a>
  </div>
  <div class="card" style="left:581px">
    <svg width="64" height="56" viewBox="0 0 64 56" fill="none" stroke="var(--icon)" stroke-width="5"><path d="M2 4h10l10 34h36l4-26H16"/><path d="M26 18h30M27 26h28" stroke-width="3"/><circle cx="28" cy="49" r="4" fill="var(--icon)"/><circle cx="54" cy="49" r="4" fill="var(--icon)"/></svg>
    <h3>Media Buying</h3>
    <p>Lorem ipsum dolor sit amet, consectetur adipiscing elit, sed do eiusmod tempor incididunt</p>
    <a class="btn" href="#">Read More</a>
  </div>
  <div class="card" style="left:791px">
    <svg width="64" height="62" viewBox="0 0 64 62"><rect x="2" y="2" width="56" height="40" rx="2" fill="var(--icon)"/><rect x="7" y="7" width="46" height="30" fill="#fff"/><circle cx="30" cy="22" r="8" fill="none" stroke="var(--icon)" stroke-width="2.5"/><path d="M26 42h8v8h8v4H18v-4h8z" fill="var(--icon)"/><rect x="50" y="40" width="12" height="20" rx="6" fill="var(--icon)"/></svg>
    <h3>Design and Social</h3>
    <p>Lorem ipsum dolor sit amet, consectetur adipiscing elit, sed do eiusmod tempor incididunt</p>
    <a class="btn" href="#">Read More</a>
  </div>
</section>

<section>
  <div class="video" role="img" aria-label="Video still: colourful illustrated gears with figures on a dark wood background">
    <svg class="play" width="44" height="44" viewBox="0 0 44 44"><circle cx="22" cy="22" r="21" fill="rgba(255,255,255,.25)"/><path d="M16 11l17 11-17 11z" fill="#fff"/></svg>
  </div>
  <div class="welcome">
    <h2>Welcome To Halvern</h2>
    <h4>Our Target Clients are Professional Service firms such as Lawyers or CPAs.</h4>
    <p>Lorem ipsum dolor sit amet, consectetur adipiscing elit, sed do eiusmod tempor incididunt ut labore et dolore magna aliqua. Ut enim ad minim veniam, quis nostrud exercitation ullamco laboris nisi ut aliquip ex ea commodo consequat. Duis aute irure dolor in reprehenderit in voluptate velit esse cillum dolore eu fugiat nulla pariatur. Excepteur sint</p>
  </div>
  <div class="news">
    <h2>Latest News</h2>
    <div class="item" style="top:51px">
      <div class="date"><b>15</b><span>Sep</span></div>
      <h5>Vestibulum ante ipsum primis in</h5>
      <p>Lorem ipsum dolor sit amet, consectetur adipiscing elit, sed do eiusmod tempor incididunt ut labore et</p>
    </div>
    <div class="item" style="top:142px">
      <div class="date"><b>15</b><span>Sep</span></div>
      <h5>Vestibulum ante ipsum primis in</h5>
      <p>Lorem ipsum dolor sit amet, consectetur adipiscing elit, sed do eiusmod tempor incididunt ut labore et</p>
    </div>
  </div>
</section>

<footer class="footer">
  <div class="copy">©2014 Halvern, Inc , All Rights Reserved.</div>
  <div class="flinks"><a href="#">Home</a><i>|</i><a href="#">Services</a><i>&nbsp;&nbsp;|</i><a href="#">Experience</a><i>|</i><a href="#">Bios</a><i>|</i><a href="#">Contact</a></div>
  <div class="fsocial"><span></span><span></span><span></span></div>
</footer>
</body>
</html>
```